Facial Tissue Brand Logo and Design

We would like you to design a Logo for the Facial Tissue Brand "Velora" along with the box design. The pack should indicate the pack size (150 x 2 ply). Also our company logo should be present (attached) along with a barcode. The box size dimensions should be 210mm (L) x 110mm (W) x 70mm (H). We are open to all kinds of nice designs which are attractive but not overdone. Happy designing!

UPDATE:
We appreciate the designs so far... but would also love to see more options in a simple and elegent design style that would look good on a table... please see attached below links for reference purpose:

www.pixmarrow.com/image-photo/cleaning-wipes-isolated-on-white-480215736

www.pixmarrow.com/image-photo/cleaning-wipes-isolated-on-white-692048153

www.pixmarrow.com/image-photo/delicate-female-hands-pulling-tissue-out-2875013649

Happy desgining!

We appreciate the designs so far.. but would like to to see some more options.

```html
<!DOCTYPE html>
<html lang="en">
<head>
<meta charset="utf-8">
<title>Velora Facial Tissue – Brand and Box Dieline</title>
<link rel="stylesheet" href="https://fonts.googleapis.com/css2?family=Archivo+Black&family=Rubik:wght@500;700&display=swap">
<style>
  :root{
    --navy:#1e4270;
    --brand-blue:#3f86c6;
    --corp-blue:#2e6fb4;
    --pale:#eef4fc;
    --mid:#a9c4ee;
    --deep:#4f82dc;
    --line:#2a2a2a;
    --paper:#ffffff;
  }
  *{box-sizing:border-box;margin:0;padding:0}
  html,body{width:1200px;height:2400px;overflow:hidden;background:var(--paper)}
  body{position:relative;font-family:"Rubik",Arial,sans-serif}

  /* brand lockup */
  .brand-lockup{position:absolute;left:0;top:0;width:1200px;height:760px}
  .brand-lockup .brand-mark{position:absolute;left:250px;top:278px;width:175px;height:175px;border-radius:50%;background:var(--brand-blue)}
  .brand-lockup .brand-name{position:absolute;left:505px;top:292px;font:500 150px/1 "Rubik",Arial,sans-serif;color:var(--brand-blue)}
  .product-title{font-family:"Archivo Black","Arial Black",sans-serif;color:var(--navy);line-height:1;white-space:nowrap}
  .brand-lockup .product-title{position:absolute;left:290px;top:496px;font-size:130px}
  .brand-lockup .product-title span{display:block}
  .brand-lockup .line-1{letter-spacing:30px}
  .brand-lockup .line-2{letter-spacing:28px;margin-top:-8px}

  /* dieline */
  .panel{position:absolute;border:1px solid var(--line);overflow:hidden}
  .panel-top{left:325px;top:1606px;width:595px;height:200px}
  .panel-main{left:325px;top:1805px;width:595px;height:312px}
  .panel-left{left:127px;top:1805px;width:199px;height:312px}
  .panel-right{left:919px;top:1805px;width:199px;height:312px}
  .panel-bottom{left:325px;top:2116px;width:595px;height:198px}

  .face-bright{background:linear-gradient(115deg,var(--paper) 0%,var(--pale) 35%,var(--mid) 70%,var(--deep) 100%)}
  .face-main{background:linear-gradient(100deg,var(--mid) 0%,var(--pale) 50%,var(--paper) 100%)}
  .face-side{background:linear-gradient(160deg,var(--paper) 0%,var(--pale) 55%,var(--mid) 100%)}

  .content{position:absolute}
  .content-wide{left:0;top:0;width:595px;height:198px}
  .content-top{transform:rotate(180deg)}
  .content-side{left:-56px;top:56px;width:311px;height:199px}
  .content-left{transform:rotate(90deg)}
  .content-right{transform:rotate(-90deg)}

  .logo{position:absolute;display:flex;align-items:center;gap:14px;white-space:nowrap}
  .logo .mark{border-radius:50%;background:var(--brand-blue);flex:none}
  .logo .name{font-weight:500;color:var(--brand-blue);line-height:1}

  .title-small{position:absolute;font-size:48px}
  .title-small span{display:block}
  .title-small .line-1{letter-spacing:8px}
  .title-small .line-2{letter-spacing:8px;margin-top:-4px}
  .title-left{font-size:25px}
  .title-left .line-1,.title-left .line-2{letter-spacing:5px}
  .title-left .line-2{margin-top:-2px}
  .title-right{font-size:20px}
  .title-right .line-1,.title-right .line-2{letter-spacing:3px}
  .title-right .line-2{margin-top:-1px}

  .pack-badge{position:absolute;display:flex;align-items:center;justify-content:center}
  .pack-badge svg{position:absolute;inset:0;width:100%;height:100%}
  .pack-badge span{position:relative;font-weight:700;font-size:20px;color:var(--paper);white-space:nowrap}
  .pack-badge.small span{font-size:17px}

  .company{position:absolute;color:var(--corp-blue);text-align:center}
  .company .square{display:block;width:20px;height:20px;background:var(--corp-blue);margin:0 auto 6px}
  .company .company-name{display:block;font-weight:500;font-size:9px;letter-spacing:.3px;white-space:nowrap}
  .company .company-place{display:block;font-weight:500;font-size:5px;letter-spacing:1.5px;white-space:nowrap}

  .photo{position:absolute;left:0;top:0;width:182px;height:100%;background:linear-gradient(160deg,#3b2a22 0%,#7a5544 30%,#e9bfa4 60%,#f3d6c3 100%)}
  .dispenser-opening{position:absolute;left:164px;top:107px;width:267px;height:92px;border:1.5px solid var(--line);border-radius:46px}

  .certs{position:absolute;display:flex;gap:6px;align-items:center}
  .certs i{display:block;width:12px;height:12px;border:1.2px solid #333}
  .certs i.round{border-radius:50%}
</style>
</head>
<body>

<header class="brand-lockup">
  <div class="brand-mark"></div>
  <div class="brand-name">Velora</div>
  <h1 class="product-title"><span class="line-1">FACIAL</span><span class="line-2">TISSUE</span></h1>
</header>

<main class="box-dieline">

  <section class="panel panel-top face-bright">
    <div class="content content-wide content-top face-bright">
      <div class="logo" style="left:20px;top:42px"><i class="mark" style="width:62px;height:62px"></i><span class="name" style="font-size:58px">Velora</span></div>
      <div class="company" style="left:10px;top:128px"><i class="square"></i><span class="company-name">NORVANE TRADING FZC</span></div>
      <div class="title-small product-title" style="left:322px;top:26px"><span class="line-1">FACIAL</span><span class="line-2">TISSUE</span></div>
      <div class="pack-badge" style="left:236px;top:127px;width:130px;height:48px">
        <svg viewBox="0 0 130 48" preserveAspectRatio="none"><path d="M4 44 C20 6 92 -4 127 7 C112 44 44 54 4 44 Z" fill="var(--navy)"/></svg>
        <span>150 x 2 ply</span>
      </div>
    </div>
  </section>

  <section class="panel panel-left face-side">
    <div class="content content-side content-left face-side">
      <div class="pack-badge small" style="left:9px;top:26px;width:122px;height:56px">
        <svg viewBox="0 0 130 48" preserveAspectRatio="none"><path d="M4 44 C20 6 92 -4 127 7 C112 44 44 54 4 44 Z" fill="var(--navy)"/></svg>
        <span>150 x 2 ply</span>
      </div>
      <div class="logo" style="left:150px;top:12px;gap:8px"><i class="mark" style="width:28px;height:28px"></i><span class="name" style="font-size:34px">Velora</span></div>
      <div class="title-small title-left product-title" style="left:152px;top:56px"><span class="line-1">FACIAL</span><span class="line-2">TISSUE</span></div>
      <div class="company" style="left:136px;top:128px"><i class="square"></i><span class="company-name">NORVANE TRADING FZC</span><span class="company-place">SHARJAH FREE ZONE</span></div>
      <div class="certs" style="left:250px;top:158px"><i></i><i class="round"></i><i class="round"></i></div>
    </div>
  </section>

  <section class="panel panel-main face-main">
    <div class="photo" role="img" aria-label="Photo of a smiling woman with closed eyes touching her cheek"></div>
    <div class="logo" style="left:310px;top:20px;gap:14px"><i class="mark" style="width:62px;height:62px"></i><span class="name" style="font-size:58px">Velora</span></div>
    <div class="dispenser-opening"></div>
    <div class="title-small product-title" style="left:322px;top:210px"><span class="line-1">FACIAL</span><span class="line-2">TISSUE</span></div>
    <div class="pack-badge" style="left:102px;top:253px;width:120px;height:46px">
      <svg viewBox="0 0 130 48" preserveAspectRatio="none"><path d="M4 44 C20 6 92 -4 127 7 C112 44 44 54 4 44 Z" fill="var(--navy)"/></svg>
      <span>150 x 2 ply</span>
    </div>
  </section>

  <section class="panel panel-right face-side">
    <div class="content content-side content-right face-side">
      <div class="pack-badge small" style="left:12px;top:75px;width:122px;height:58px">
        <svg viewBox="0 0 130 48" preserveAspectRatio="none"><path d="M4 44 C20 6 92 -4 127 7 C112 44 44 54 4 44 Z" fill="var(--navy)"/></svg>
        <span>150 x 2 ply</span>
      </div>
      <div class="logo" style="left:160px;top:66px;gap:7px"><i class="mark" style="width:24px;height:24px"></i><span class="name" style="font-size:28px">Velora</span></div>
      <div class="title-small title-right product-title" style="left:168px;top:104px"><span class="line-1">FACIAL</span><span class="line-2">TISSUE</span></div>
    </div>
  </section>

  <section class="panel panel-bottom face-bright">
    <div class="content content-wide">
      <div class="logo" style="left:20px;top:42px"><i class="mark" style="width:62px;height:62px"></i><span class="name" style="font-size:58px">Velora</span></div>
      <div class="company" style="left:14px;top:128px"><i class="square"></i><span class="company-name">NORVANE TRADING FZC</span><span class="company-place">SHARJAH FREE ZONE</span></div>
      <div class="title-small product-title" style="left:322px;top:26px"><span class="line-1">FACIAL</span><span class="line-2">TISSUE</span></div>
      <div class="pack-badge" style="left:236px;top:127px;width:130px;height:48px">
        <svg viewBox="0 0 130 48" preserveAspectRatio="none"><path d="M4 44 C20 6 92 -4 127 7 C112 44 44 54 4 44 Z" fill="var(--navy)"/></svg>
        <span>150 x 2 ply</span>
      </div>
    </div>
  </section>

</main>
</body>
</html>
```